Quorvane Capital Modern Business Card

We need a modern business card template designed for Quorvane Capital.
Quorvane Capital is a diversified global cryptocurrency investment fund.

The font under the logo: Hiragino Kaku Gothic Pro

Color Hexcode: Main colors white (ffffff) & teal (188383), we are open to adding #fcca46 as an accent

Target Market(s)

Accredited Investors, high net worth individuals and institutional investors

Industry/Entity Type

Investment

Contact Information for Business Card

Contact Information should contain
Name
main phone +1 720 555 0147
cell
email

Font styles to use
Sans Serif
Other font styles liked:
• Hiragino Kaku Gothic Pro

Requirements
Must have
• would like to have icons that identify the contact information
• include our website: www.quorvanecapital.example
• include our Tagline: Diversified Crypto Investment Funds
Nice to have
• Would like to have a simple back side with the logo (without the words) and plenty of space

```html
<!DOCTYPE html>
<html lang="en">
<head>
<meta charset="utf-8">
<title>Quorvane Capital Business Card</title>
<link href="https://fonts.googleapis.com/css2?family=Questrial&display=swap" rel="stylesheet">
<style>
  :root {
    --backdrop: #c9cacb;
    --card: #f7f7f5;
    --teal: #188383;
    --ink: #1d1d1d;
    --edge: rgba(0,0,0,0.18);
  }
  * { margin: 0; padding: 0; box-sizing: border-box; }
  html, body { width: 1200px; height: 1200px; overflow: hidden; }
  body {
    background: var(--backdrop);
    font-family: "Questrial", "Century Gothic", sans-serif;
    color: var(--ink);
    position: relative;
  }
  .card {
    position: absolute;
    left: 250px;
    width: 700px;
    height: 400px;
    background: var(--card);
    box-shadow: 0 10px 24px var(--edge);
  }
  .card--back { top: 150px; }
  .card--front { top: 640px; }

  .back-mark {
    position: absolute;
    inset: 0;
    display: flex;
    align-items: center;
    justify-content: center;
    gap: 18px;
  }
  .back-mark__dot {
    width: 22px; height: 22px; border-radius: 50%;
    background: var(--teal);
  }
  .back-mark__name {
    font-size: 44px;
    color: var(--teal);
    letter-spacing: 2px;
  }

  .brand {
    position: absolute;
    left: 54px; top: 92px;
    display: flex; align-items: center; gap: 12px;
  }
  .brand__square { width: 16px; height: 16px; background: var(--teal); }
  .brand__name { font-size: 24px; color: var(--ink); letter-spacing: 0.5px; text-transform: uppercase; }

  .person { position: absolute; right: 48px; top: 42px; text-align: right; }
  .person__name { font-size: 30px; font-weight: 400; -webkit-text-stroke: 0.6px var(--ink); }
  .person__title { font-size: 17px; margin-top: 2px; }

  .contact {
    position: absolute;
    left: 350px; top: 140px;
    list-style: none;
    font-size: 19px;
    line-height: 1.25;
  }
  .contact__item { display: flex; align-items: flex-start; gap: 10px; margin-bottom: 3px; }
  .contact__icon { width: 20px; height: 20px; flex: none; margin-top: 2px; }
  .contact__text--indent { padding-left: 30px; margin-top: -3px; margin-bottom: 8px; }

  .tagline {
    position: absolute;
    left: 40px; bottom: 34px;
    font-size: 27px;
    color: var(--teal);
    letter-spacing: 4.5px;
  }
</style>
</head>
<body>

<section class="card card--back" aria-label="Card back">
  <div class="back-mark">
    <span class="back-mark__dot"></span>
    <span class="back-mark__name">Quorvane Capital</span>
  </div>
</section>

<section class="card card--front" aria-label="Card front">
  <div class="brand">
    <span class="brand__square"></span>
    <span class="brand__name">Quorvane Capital</span>
  </div>

  <div class="person">
    <h1 class="person__name">Your Full Name</h1>
    <p class="person__title">Your Title</p>
  </div>

  <ul class="contact">
    <li class="contact__item">
      <svg class="contact__icon" viewBox="0 0 20 20"><circle cx="10" cy="10" r="10" fill="#188383"/><path d="M5 10.5 10 6l5 4.5M6.8 9.5V14h6.4V9.5" fill="none" stroke="#fff" stroke-width="1.6"/></svg>
      <span>Your address line 1</span>
    </li>
    <li class="contact__text--indent">Your address line 2</li>
    <li class="contact__item">
      <svg class="contact__icon" viewBox="0 0 20 20"><circle cx="10" cy="10" r="10" fill="#188383"/><path d="M6.5 5.5c-1 1 0 4 2.5 6.5s5.5 3.5 6.5 2.5l-2-2-1.5 1c-1.5-.7-3-2.2-3.7-3.7l1-1.5z" fill="#fff"/></svg>
      <span>+1 720 555 0147</span>
    </li>
    <li class="contact__item">
      <svg class="contact__icon" viewBox="0 0 20 20"><circle cx="10" cy="10" r="10" fill="#188383"/><rect x="7" y="4.5" width="6" height="11" rx="1" fill="#fff"/><rect x="8" y="6" width="4" height="6.5" fill="#188383"/></svg>
      <span>123 456 7890</span>
    </li>
    <li class="contact__item">
      <svg class="contact__icon" viewBox="0 0 20 20"><circle cx="10" cy="10" r="10" fill="#188383"/><rect x="5" y="6.5" width="10" height="7" fill="#fff"/><path d="M5 6.5 10 10.5 15 6.5" fill="none" stroke="#188383" stroke-width="1.2"/></svg>
      <span>Your email@quorvanecapital.example</span>
    </li>
    <li class="contact__item">
      <svg class="contact__icon" viewBox="0 0 20 20"><circle cx="10" cy="10" r="10" fill="#188383"/><g fill="none" stroke="#fff" stroke-width="1.1"><circle cx="10" cy="10" r="5.5"/><ellipse cx="10" cy="10" rx="2.4" ry="5.5"/><path d="M4.5 10h11"/></g></svg>
      <span>www.quorvanecapital.example</span>
    </li>
  </ul>

  <p class="tagline">Diversified Crypto Investment Funds</p>
</section>

</body>
</html>
```